Business Card Design for Contracting

I need a Busines card design for a new Busines (sole trader) based in Sydney, Australia. The business has been set up so I can contract my services to companies. The service I provide is mainly in the civil engineering discipline with the services that can be provided being contract project management, contract estimating, contract time controls and contract financial controls. I would like the design to have the colour blue used.

Target Market(s)

Large to medium Construction companies.

Industry/Entity Type

Construction

Contact Information for Business Card

Penrose Civil Engineering Services
P.O. Box 318
Marlow Ridge, NSW, 1892

Mobile: 0412 586 293

Email: oscar.penrose@pces.example.au
Web: PCES.example.au

Font styles to use
Sans Serif

Colors
0493ce
34a6d7
85cae6

Requirements
Must have
• my project must have my name and qualification:
• Oscar Penhallow
• BE (Civil), MTRGuild.

```html
<!DOCTYPE html>
<html lang="en">
<head>
<meta charset="utf-8">
<title>Penrose Civil Engineering Services – Business Card</title>
<link href="https://fonts.googleapis.com/css2?family=Open+Sans:wght@400;600&family=Roboto+Condensed:wght@700&display=swap" rel="stylesheet">
<style>
  :root {
    --page-bg: #e8e5e1;
    --card-bg: #ffffff;
    --brand-blue: #0b84bd;
    --band-blue: #0a87bf;
    --text-grey: #808080;
    --band-text: #ffffff;
  }
  * { margin: 0; padding: 0; box-sizing: border-box; }
  html, body {
    width: 1200px; height: 1000px; overflow: hidden;
    background: var(--page-bg);
    font-family: "Open Sans", Arial, sans-serif;
  }
  .canvas { position: relative; width: 1200px; height: 1000px; }
  .card {
    position: absolute; left: 265px; width: 665px; height: 397px;
    background: var(--card-bg); border-radius: 22px; overflow: hidden;
    box-shadow: 0 3px 8px rgba(0,0,0,0.18);
  }
  .card--first { top: 73px; }
  .card--second { top: 532px; }
  .brand-name {
    position: absolute; top: 142px; left: 0; width: 100%;
    line-height: 36px; text-align: center; color: var(--brand-blue);
    font-family: "Open Sans", Arial, sans-serif; font-weight: 600;
    font-size: 27px; letter-spacing: 0.5px; white-space: nowrap;
  }
  .holder {
    position: absolute; top: 256px; left: 0; width: 100%; line-height: 28px;
    text-align: center; color: var(--brand-blue); white-space: nowrap;
  }
  .holder__name {
    font-family: "Roboto Condensed", Arial, sans-serif; font-weight: 700; font-size: 22px;
  }
  .holder__qual { font-size: 16px; margin-left: 4px; }
  .contact {
    position: absolute; left: 0; width: 100%; text-align: center;
    color: var(--text-grey); white-space: nowrap;
  }
  .contact--phone { top: 297px; font-size: 17px; line-height: 24px; }
  .contact--email { top: 322px; font-size: 15px; line-height: 22px; }
  .address-band {
    position: absolute; left: 0; bottom: 0; width: 100%; height: 43px;
    padding-bottom: 7px;
    background: var(--band-blue); color: var(--band-text);
    display: flex; align-items: center; justify-content: center;
    font-size: 16.5px; white-space: nowrap;
  }
  .address-band .sep { margin: 0 11px; }
</style>
</head>
<body>
<main class="canvas">
  <section class="card card--first">
    <div class="brand-name">Penrose Civil Engineering Services</div>
    <div class="holder"><span class="holder__name">Oscar Penhallow</span><span class="holder__qual">/ BE (Civil), MTRGuild.</span></div>
    <div class="contact contact--phone">0412 586 293</div>
    <div class="contact contact--email">oscar@penrose.example.au</div>
    <div class="address-band">P.O. Box 318<span class="sep">|</span>Marlow Ridge<span class="sep">|</span>NSW<span class="sep">|</span>1892</div>
  </section>
  <section class="card card--second">
    <div class="brand-name">Penrose Civil Engineering Services</div>
    <div class="holder"><span class="holder__name">Oscar Penhallow</span><span class="holder__qual">/ BE (Civil), MTRGuild.</span></div>
    <div class="contact contact--phone">0412 586 293</div>
    <div class="contact contact--email">oscar@penrose.example.au</div>
    <div class="address-band">P.O. Box 318<span class="sep">|</span>Marlow Ridge<span class="sep">|</span>NSW<span class="sep">|</span>1892</div>
  </section>
</main>
</body>
</html>
```